New Website Announcement

We need a flyer to announce our new website to customers and prospective clients. The website will be launching soon, but I can provide a detailed outline in PDF form with copy and imagery to serve as inspiration for this design.

I would like a postcard size document that can be mailed in an envelope (no need for postcard style mailer info on 1 side)

About my company:

Clearwater Lantern Group is a new breed of marketing consulting agency built for the next frontier of consumer learning. Social interaction will be at the heart of great insights going forward – in how consumers engage with brands and in how organizations socialize what they learn to gain competitive advantage.
By fusing innovative insights techniques, technology and compelling graphic design-based reporting, we ensure results get noticed and make an impact.

contact info that can also be included:

Email: morgan@clearwater-lantern.com

Phone: 518-732-6148

New High Res logo file has been added. (.ai)

Thanks

Reason: Giving more time next week for submissions. This project has been committed. Thanks !

Attention all designers submitting a design for this project. Please keep in mind a few important details about this project.

1. Remember that the main objective of this postcard is to announce my new website.

2. Please be sure to read the brief for the copy I would like on each side. You can be creative in how it is displayed, but I need this key information somewhere. All other copy on the attached files is for your background only.

3. Please do not submit overly simple designs that just take the images I provided and overlay a text box with my copy. I could easily do this myself in PowerPoint in 5 minutes.

4. Remember that the design should be edgy and modern but needs to be professional and speak to a business audience.

Please submit any questions. Thank you for your submissions. 

Morgan

Illustrator high res logo file now correctly uploaded. Thanks.

Target Market(s)

senior level marketing and research clients at large companies and agencies

Industry/Entity Type

Marketing

Requirements
Must have
• Main message:

Need an engaging way to tell customers and prospective clients that we have a new website and that they should come visit us online to learn more about out services, check out case studies and read about our exciting partnerships.

COPY TO USE - UPDATED

Side 1:
(logo)
Introducing Clearwater Lantern Group

Let’s talk about taking research out of the dark ages.

Visit our newly launched website to learn how and get in touch.

www.clearwater-lantern.com

Side 2
Logo
followed by tagline:
Consumer insights that get noticed.
A leading-edge marketing partnership that really works.

Additional text to use on Side 2:
How we can help...

Think of us as your go-to resource for identifying and incorporating the most innovative and exciting techniques into your research programs. We carefully curate and develop close partnerships with the best of the best - from online qualitative research and mobile ethnography to social media listening and fresh takes on concept testing, we can guide the way.

Plus, we believe that socializing consumer learning is just as critical as gathering it.By taking insights deliverables to the next level – through infographics, videos, magazines,interactive profiles and so much more – we are getting stakeholders excited to engage with research and inspired to take action because of it.
It’s a new way to look at insights from a new type of partner. And, it’s a new way to get the most from your research dollars.
Nice to have
• could incorporate our website main image of the lamp on white brick background which is attached, but not 100% mandatory.
Should not have
• - should not be too playful or young, but needs to be modern and design focused

- should not be cluttered or overly 'salesy'

- needs to be upscale and elegant / compelling and aligned with the look and feel of the website imagery (see attached)

```html
<!DOCTYPE html>
<html lang="en">
<head>
<meta charset="utf-8">
<title>Clearwater Lantern Group – New Website Announcement</title>
<link href="https://fonts.googleapis.com/css2?family=Fira+Sans+Condensed:wght@600;800&family=Open+Sans:wght@400;600&display=swap" rel="stylesheet">
<style>
  :root {
    --page: #ffffff;
    --backdrop: #f4f4f4;
    --ink: #111111;
    --band: #141414;
    --brand-blue: #1a7fc4;
    --ribbon-dark: #0e2a44;
    --wall-glow: #ffffff;
    --wall-light: #eeeeec;
    --wall-mid: #cfcfcc;
    --wall-shade: #a9a9a6;
    --floor-edge: #8f8f8c;
    --floor: #c4c4c1;
    --text-light: #ffffff;
    --contact: #1c1c1c;
  }
  * { box-sizing: border-box; margin: 0; padding: 0; }
  html, body { width: 1200px; height: 882px; overflow: hidden; background: var(--backdrop); }

  .postcard { position: relative; width: 1200px; height: 882px; }
  .postcard__sheet {
    position: absolute; left: 32px; top: 32px; width: 1136px; height: 818px;
    background: var(--page);
    box-shadow: 0 2px 10px rgba(0,0,0,.35);
  }

  .hero-photo {
    position: absolute; left: 118px; top: 190px; width: 964px; height: 578px;
    background:
      radial-gradient(ellipse 300px 220px at 380px 120px, rgba(255,255,255,1), rgba(255,255,255,0) 75%),
      radial-gradient(ellipse 700px 420px at 420px 200px, rgba(255,255,255,.55), rgba(255,255,255,0) 70%),
      linear-gradient(90deg, rgba(0,0,0,.18) 0%, rgba(0,0,0,0) 18%, rgba(0,0,0,0) 80%, rgba(0,0,0,.14) 100%),
      linear-gradient(180deg,
        var(--wall-mid) 0%, var(--wall-light) 18%, var(--wall-light) 55%,
        var(--wall-mid) 74%, var(--wall-shade) 79%, var(--floor-edge) 80.5%,
        var(--floor) 84%, #d2d2cf 100%);
  }

  .headline-band {
    position: absolute; left: 118px; top: 118px; width: 964px; height: 72px;
    background: var(--band);
    box-shadow: 0 3px 6px rgba(0,0,0,.35);
  }
  .headline-band__text {
    position: absolute; left: 195px; top: 122px;
    font-family: "Fira Sans Condensed", "Arial Narrow", sans-serif;
    font-weight: 600; font-size: 25px; line-height: 32px;
    color: var(--text-light);
  }

  .brand-block { position: absolute; left: 322px; top: 368px; width: 420px; }
  .brand-block__intro {
    font-family: "Open Sans", Arial, sans-serif;
    font-weight: 600; font-size: 20px; line-height: 28px;
    letter-spacing: 3px; text-transform: uppercase;
    color: var(--ink);
  }
  .brand-block__name {
    margin-top: 6px;
    font-family: "Fira Sans Condensed", "Arial Narrow", sans-serif;
    font-weight: 800; font-size: 64px; line-height: 74px;
    text-transform: uppercase; letter-spacing: 1px;
    color: var(--brand-blue);
    white-space: nowrap;
  }

  .contact {
    position: absolute; right: 145px; top: 696px;
    font-family: "Open Sans", Arial, sans-serif;
    font-style: normal; font-weight: 400;
    font-size: 18px; line-height: 31px; color: var(--contact);
    text-align: right;
  }
  .contact__line { display: flex; align-items: center; justify-content: flex-end; gap: 8px; }
  .contact__icon { width: 22px; height: 18px; }

  .overlay { position: absolute; left: 0; top: 0; }
</style>
</head>
<body>
<main class="postcard">
  <div class="postcard__sheet"></div>

  <div class="hero-photo" role="img" aria-label="Arched black floor lamp glowing against a whitewashed brick wall above a concrete floor"></div>

  <div class="headline-band"></div>
  <p class="headline-band__text">Let’s talk about taking research out of the dark ages.<br>Visit our newly launched website to learn how and get in touch.</p>

  <div class="brand-block">
    <p class="brand-block__intro">Introducing</p>
    <h1 class="brand-block__name">Clearwater<br>Lantern Group</h1>
  </div>

  <address class="contact">
    <div class="contact__line">
      <svg class="contact__icon" viewBox="0 0 22 18" aria-hidden="true"><rect x="1" y="2" width="20" height="14" fill="none" stroke="#1c1c1c" stroke-width="1.6"/><path d="M1 2l10 8 10-8" fill="none" stroke="#1c1c1c" stroke-width="1.6"/></svg>
      <span>morgan@clearwater-lantern.com</span>
    </div>
    <div class="contact__line">
      <svg class="contact__icon" viewBox="0 0 22 20" aria-hidden="true"><path d="M5 1c1 0 3 4 3 5s-2 2-2 3c1 3 3 5 6 6 1 0 2-2 3-2s5 2 5 3c0 2-2 4-4 4C8 20 1 12 1 5c0-2 2-4 4-4z" fill="#1c1c1c"/></svg>
      <span>518-732-6148</span>
    </div>
  </address>

  <svg class="overlay" width="1200" height="882" viewBox="0 0 1200 882" aria-hidden="true">
    <defs>
      <linearGradient id="badge-blue" x1="0" y1="0" x2="0" y2="1">
        <stop offset="0" stop-color="#4aa3e6"/>
        <stop offset="1" stop-color="#1668b5"/>
      </linearGradient>
      <linearGradient id="ribbon-fill" x1="0" y1="0" x2="1" y2="0">
        <stop offset="0" stop-color="#1f6fb8"/>
        <stop offset=".5" stop-color="#3592d8"/>
        <stop offset="1" stop-color="#2479c2"/>
      </linearGradient>
      <filter id="soft-shadow" x="-20%" y="-20%" width="140%" height="140%">
        <feDropShadow dx="0" dy="2" stdDeviation="3" flood-color="#000" flood-opacity=".4"/>
      </filter>
    </defs>

    <g class="pointer-badge" filter="url(#soft-shadow)">
      <circle cx="143" cy="152" r="50" fill="#ffffff"/>
      <circle cx="143" cy="152" r="40" fill="url(#badge-blue)"/>
      <path d="M133 130l0 38 9-8 6 13 6-3-6-12 12-1z" fill="none" stroke="#ffffff" stroke-width="3" stroke-linejoin="round"/>
    </g>

    <polygon class="ribbon-fold" points="1082,300 1082,348 1058,322" fill="#0e2a44"/>

    <g class="web-ribbon" transform="translate(993 200) rotate(45)" filter="url(#soft-shadow)">
      <rect x="-180" y="-28" width="360" height="56" fill="url(#ribbon-fill)"/>
      <text x="0" y="9" text-anchor="middle"
            font-family="'Fira Sans Condensed', 'Arial Narrow', sans-serif"
            font-weight="800" font-size="26" fill="#ffffff">www.clearwater-lantern.com</text>
    </g>
  </svg>
</main>
</body>
</html>
```